依頼詳細
今回の企画はA5横「付箋卓上カレンダー」でテンプレートに記載してあるように下部の部分に名入れ刷り込みスペースがあります。
上部の約20mmほどの部分にリングの代わりに付箋糊で積層したカレンダーで1か月使用後ははがして使います。
それ以外の場所はリングを使用していないので、すべてカレンダーとして使用できるスペースです。
カレンダーの用紙は上質紙を使用します。
台紙は通常の三角柱上になる組み立てスタンドになります。
台紙は黒またはクラフト系の用紙を使用します。
仕事の机の上において使用するカレンダーをイメージしておりますので、機能性重視です。
記載項目
卓上カレンダーデザイン
希望イメージ
シンプル 複雑
単色 カラフル
暗い 明るい
日常 高級
遊び心 厳粛
未来的 伝統的
女性的 男性的
希望する色
納品ファイル
• イラストレーター形式 (.ai)
補足説明
■ 選んだ理由

今回機能性実用性を重視いたしましたので、
メモが書ける書きやすい。
見やすい。
前後の月も確認できる。
事務机の上に置いてなじみやすい
という4点をポイントに選考いたしました。
上部に付箋の糊を使用してカレンダーを積層するA5卓上付箋カレンダーはありませんので月の表示が最上部にないものが良いのではないか、日付スペースに罫線が入ったものが書きやすくていいのではないか
という意見も多かったのですが、
最終的にバランスの良さ、目標を書くメモスペースや表紙の利用の仕方、イメージがしやすいことが当選理由となりました。

■ 提案者全員のお礼・コメント

この度は弊社の卓上付箋カレンダーのデザインコンペにご応募いただき、誠にありがとうございました。

おかげさまで採用デザインが無事決定いたしました。

初めて当システムを利用させていただきました。
いろいろ素晴らしいご提案をいただき、今後も新商品開発の際はデザインコンペを開催したいと思っております。

今回選に漏れた皆様には申し訳ございませんが、また次回にはご参加いただければ幸いです。

今後ともよろしくお願いします。

とりあえずお礼まで

```html
<!DOCTYPE html>
<html lang="ja">
<head>
<meta charset="utf-8">
<title>2020 卓上付箋カレンダー</title>
<link href="https://fonts.googleapis.com/css2?family=Noto+Sans+JP:wght@400;500;700;900&family=Roboto:wght@400;500;700&display=swap" rel="stylesheet">
<style>
:root{
  --stage:#e9e9e7;
  --paper:#ffffff;
  --ink:#3a3a3a;
  --muted:#8c8c8c;
  --band:#8a8a8a;
  --rule:#cfcfcf;
  --sun:#d9342b;
  --sat:#3a5fbf;
  --accent:#ee7a2a;
  --sun-tint:#fdeee8;
  --sat-tint:#eef1fb;
  --ghost:#f0f0f0;
}
*{box-sizing:border-box;margin:0;padding:0}
html,body{width:886px;height:1200px;overflow:hidden}
body{background:var(--stage);font-family:"Noto Sans JP",sans-serif;color:var(--ink);position:relative}
.card{position:absolute;left:20px;width:846px;background:var(--paper);box-shadow:0 1px 3px rgba(0,0,0,.15)}

/* ---------- year overview card ---------- */
.year-card{top:18px;height:566px}
.year-title{height:48px;background:var(--band);color:#fff;font-family:"Roboto",sans-serif;font-weight:700;font-size:24px;letter-spacing:3px;display:flex;align-items:center;justify-content:center}
.year-grid{display:grid;grid-template-columns:repeat(4,1fr);column-gap:26px;row-gap:12px;padding:14px 26px 0}
.mini-month{position:relative;height:112px;border-bottom:1px solid var(--rule)}
.mini-month .ghost{position:absolute;right:4px;top:-6px;font-family:"Roboto",sans-serif;font-weight:700;font-size:96px;line-height:1;color:var(--ghost);z-index:0}
.mini-month h3{position:relative;z-index:1;font-family:"Roboto",sans-serif;font-size:13px;font-weight:700;color:var(--sun);height:16px;line-height:16px}
.days{position:relative;z-index:1;display:grid;grid-template-columns:repeat(7,1fr);font-family:"Roboto",sans-serif;font-size:10px;line-height:15px;text-align:center}
.days i{font-style:normal}
.o1 i:first-child{grid-column-start:2}.o2 i:first-child{grid-column-start:3}.o3 i:first-child{grid-column-start:4}
.o4 i:first-child{grid-column-start:5}.o5 i:first-child{grid-column-start:6}.o6 i:first-child{grid-column-start:7}
.o0 i:nth-child(7n+1),.o1 i:nth-child(7n+7),.o2 i:nth-child(7n+6),.o3 i:nth-child(7n+5),.o4 i:nth-child(7n+4),.o5 i:nth-child(7n+3),.o6 i:nth-child(7n+2){color:var(--sun)}
.o0 i:nth-child(7n+7),.o1 i:nth-child(7n+6),.o2 i:nth-child(7n+5),.o3 i:nth-child(7n+4),.o4 i:nth-child(7n+3),.o5 i:nth-child(7n+2),.o6 i:nth-child(7n+1){color:var(--sat)}
.imprint{position:absolute;left:0;right:0;bottom:0;height:112px;border-top:1px solid var(--rule);display:flex;flex-direction:column;align-items:center;justify-content:center;gap:4px}
.brand{display:flex;align-items:center;gap:10px;font-weight:900;font-size:34px;color:var(--ink);letter-spacing:1px}
.brand .mark{width:18px;height:18px;background:var(--accent)}
.tagline{font-size:11px;color:var(--muted);letter-spacing:1px}

/* ---------- monthly card ---------- */
.month-card{top:600px;height:582px}
.strip{display:flex;align-items:center;height:30px;border-bottom:1px solid var(--rule);font-family:"Roboto",sans-serif;font-size:10px}
.strip .label{width:44px;height:100%;background:var(--band);color:#fff;font-family:"Noto Sans JP",sans-serif;font-weight:700;font-size:13px;display:flex;align-items:center;justify-content:center;flex:none}
.strip span{flex:1;text-align:center}
.strip .su{color:var(--sun)}.strip .sa{color:var(--sat)}
.strip.next{border-top:1px solid var(--rule);border-bottom:none}
.month-body{display:flex;height:392px;border-top:3px solid var(--accent)}
.month-side{width:150px;border-right:2px solid var(--accent);padding:12px 14px;display:flex;flex-direction:column}
.month-side .yr{font-family:"Roboto",sans-serif;font-size:11px;font-weight:500;color:var(--accent);margin-left:46px;margin-bottom:-10px}
.month-side .mo{font-size:44px;font-weight:700;color:var(--accent);line-height:1.1}
.month-side .mo small{font-size:24px}
.month-side .en{font-family:"Roboto",sans-serif;font-size:12px;color:var(--accent);margin-bottom:12px}
.memo{flex:1;border:1px solid var(--rule);background:repeating-linear-gradient(to bottom,transparent 0 21px,var(--rule) 21px 22px);background-position:0 6px}
.month-grid{flex:1;display:grid;grid-template-columns:repeat(7,1fr);grid-template-rows:22px repeat(5,1fr)}
.month-grid .wd{font-family:"Roboto",sans-serif;font-size:10px;color:var(--muted);padding:5px 6px;border-bottom:1px solid var(--rule);border-right:1px solid var(--rule)}
.month-grid .cell{border-right:1px solid var(--rule);border-bottom:1px solid var(--rule);padding:5px 7px;font-family:"Roboto",sans-serif;font-size:15px;font-weight:500}
.month-grid > :nth-child(7n+1){background:var(--sun-tint)}
.month-grid > :nth-child(7n){background:var(--sat-tint);border-right:none}
.month-grid > :nth-child(7n+1).cell,.month-grid .hol{color:var(--sun)}
.month-grid > :nth-child(7n).cell{color:var(--sat)}
.month-grid .hol small{font-size:8px;font-weight:400;margin-left:3px}
.month-grid .wd.su{color:var(--sun)}.month-grid .wd.sa{color:var(--sat)}
.month-card .imprint{height:126px;border-top:none}
</style>
</head>
<body>

<section class="card year-card">
  <header class="year-title">2020 CALENDAR</header>
  <div class="year-grid">
    <div class="mini-month"><span class="ghost">1</span><h3>1</h3><div class="days o3"><i>1</i><i>2</i><i>3</i><i>4</i><i>5</i><i>6</i><i>7</i><i>8</i><i>9</i><i>10</i><i>11</i><i>12</i><i>13</i><i>14</i><i>15</i><i>16</i><i>17</i><i>18</i><i>19</i><i>20</i><i>21</i><i>22</i><i>23</i><i>24</i><i>25</i><i>26</i><i>27</i><i>28</i><i>29</i><i>30</i><i>31</i></div></div>
    <div class="mini-month"><span class="ghost">2</span><h3>2</h3><div class="days o6"><i>1</i><i>2</i><i>3</i><i>4</i><i>5</i><i>6</i><i>7</i><i>8</i><i>9</i><i>10</i><i>11</i><i>12</i><i>13</i><i>14</i><i>15</i><i>16</i><i>17</i><i>18</i><i>19</i><i>20</i><i>21</i><i>22</i><i>23</i><i>24</i><i>25</i><i>26</i><i>27</i><i>28</i><i>29</i></div></div>
    <div class="mini-month"><span class="ghost">3</span><h3>3</h3><div class="days o0"><i>1</i><i>2</i><i>3</i><i>4</i><i>5</i><i>6</i><i>7</i><i>8</i><i>9</i><i>10</i><i>11</i><i>12</i><i>13</i><i>14</i><i>15</i><i>16</i><i>17</i><i>18</i><i>19</i><i>20</i><i>21</i><i>22</i><i>23</i><i>24</i><i>25</i><i>26</i><i>27</i><i>28</i><i>29</i><i>30</i><i>31</i></div></div>
    <div class="mini-month"><span class="ghost">4</span><h3>4</h3><div class="days o3"><i>1</i><i>2</i><i>3</i><i>4</i><i>5</i><i>6</i><i>7</i><i>8</i><i>9</i><i>10</i><i>11</i><i>12</i><i>13</i><i>14</i><i>15</i><i>16</i><i>17</i><i>18</i><i>19</i><i>20</i><i>21</i><i>22</i><i>23</i><i>24</i><i>25</i><i>26</i><i>27</i><i>28</i><i>29</i><i>30</i></div></div>
    <div class="mini-month"><span class="ghost">5</span><h3>5</h3><div class="days o5"><i>1</i><i>2</i><i>3</i><i>4</i><i>5</i><i>6</i><i>7</i><i>8</i><i>9</i><i>10</i><i>11</i><i>12</i><i>13</i><i>14</i><i>15</i><i>16</i><i>17</i><i>18</i><i>19</i><i>20</i><i>21</i><i>22</i><i>23</i><i>24</i><i>25</i><i>26</i><i>27</i><i>28</i><i>29</i><i>30</i><i>31</i></div></div>
    <div class="mini-month"><span class="ghost">6</span><h3>6</h3><div class="days o1"><i>1</i><i>2</i><i>3</i><i>4</i><i>5</i><i>6</i><i>7</i><i>8</i><i>9</i><i>10</i><i>11</i><i>12</i><i>13</i><i>14</i><i>15</i><i>16</i><i>17</i><i>18</i><i>19</i><i>20</i><i>21</i><i>22</i><i>23</i><i>24</i><i>25</i><i>26</i><i>27</i><i>28</i><i>29</i><i>30</i></div></div>
    <div class="mini-month"><span class="ghost">7</span><h3>7</h3><div class="days o3"><i>1</i><i>2</i><i>3</i><i>4</i><i>5</i><i>6</i><i>7</i><i>8</i><i>9</i><i>10</i><i>11</i><i>12</i><i>13</i><i>14</i><i>15</i><i>16</i><i>17</i><i>18</i><i>19</i><i>20</i><i>21</i><i>22</i><i>23</i><i>24</i><i>25</i><i>26</i><i>27</i><i>28</i><i>29</i><i>30</i><i>31</i></div></div>
    <div class="mini-month"><span class="ghost">8</span><h3>8</h3><div class="days o6"><i>1</i><i>2</i><i>3</i><i>4</i><i>5</i><i>6</i><i>7</i><i>8</i><i>9</i><i>10</i><i>11</i><i>12</i><i>13</i><i>14</i><i>15</i><i>16</i><i>17</i><i>18</i><i>19</i><i>20</i><i>21</i><i>22</i><i>23</i><i>24</i><i>25</i><i>26</i><i>27</i><i>28</i><i>29</i><i>30</i><i>31</i></div></div>
    <div class="mini-month"><span class="ghost">9</span><h3>9</h3><div class="days o2"><i>1</i><i>2</i><i>3</i><i>4</i><i>5</i><i>6</i><i>7</i><i>8</i><i>9</i><i>10</i><i>11</i><i>12</i><i>13</i><i>14</i><i>15</i><i>16</i><i>17</i><i>18</i><i>19</i><i>20</i><i>21</i><i>22</i><i>23</i><i>24</i><i>25</i><i>26</i><i>27</i><i>28</i><i>29</i><i>30</i></div></div>
    <div class="mini-month"><span class="ghost">10</span><h3>10</h3><div class="days o4"><i>1</i><i>2</i><i>3</i><i>4</i><i>5</i><i>6</i><i>7</i><i>8</i><i>9</i><i>10</i><i>11</i><i>12</i><i>13</i><i>14</i><i>15</i><i>16</i><i>17</i><i>18</i><i>19</i><i>20</i><i>21</i><i>22</i><i>23</i><i>24</i><i>25</i><i>26</i><i>27</i><i>28</i><i>29</i><i>30</i><i>31</i></div></div>
    <div class="mini-month"><span class="ghost">11</span><h3>11</h3><div class="days o0"><i>1</i><i>2</i><i>3</i><i>4</i><i>5</i><i>6</i><i>7</i><i>8</i><i>9</i><i>10</i><i>11</i><i>12</i><i>13</i><i>14</i><i>15</i><i>16</i><i>17</i><i>18</i><i>19</i><i>20</i><i>21</i><i>22</i><i>23</i><i>24</i><i>25</i><i>26</i><i>27</i><i>28</i><i>29</i><i>30</i></div></div>
    <div class="mini-month"><span class="ghost">12</span><h3>12</h3><div class="days o2"><i>1</i><i>2</i><i>3</i><i>4</i><i>5</i><i>6</i><i>7</i><i>8</i><i>9</i><i>10</i><i>11</i><i>12</i><i>13</i><i>14</i><i>15</i><i>16</i><i>17</i><i>18</i><i>19</i><i>20</i><i>21</i><i>22</i><i>23</i><i>24</i><i>25</i><i>26</i><i>27</i><i>28</i><i>29</i><i>30</i><i>31</i></div></div>
  </div>
  <footer class="imprint">
    <div class="brand"><span class="mark"></span>メモ日和.net</div>
    <p class="tagline">毎日の机にそっと寄りそうメモ文具</p>
  </footer>
</section>

<section class="card month-card">
  <div class="strip prev">
    <span class="label">12月</span>
    <span class="su">1</span><span>2</span><span>3</span><span>4</span><span>5</span><span>6</span><span class="sa">7</span><span class="su">8</span><span>9</span><span>10</span><span>11</span><span>12</span><span>13</span><span class="sa">14</span><span class="su">15</span><span>16</span><span>17</span><span>18</span><span>19</span><span>20</span><span class="sa">21</span><span class="su">22</span><span>23</span><span>24</span><span>25</span><span>26</span><span>27</span><span class="sa">28</span><span class="su">29</span><span>30</span><span>31</span>
  </div>
  <div class="month-body">
    <aside class="month-side">
      <p class="yr">2020</p>
      <p class="mo">1<small>月</small></p>
      <p class="en">January</p>
      <div class="memo" aria-label="メモ欄"></div>
    </aside>
    <div class="month-grid">
      <div class="wd su">Su</div><div class="wd">Mo</div><div class="wd">Tu</div><div class="wd">We</div><div class="wd">Th</div><div class="wd">Fr</div><div class="wd sa">Sa</div>
      <div class="cell"></div><div class="cell"></div><div class="cell"></div><div class="cell hol">1</div><div class="cell">2</div><div class="cell">3</div><div class="cell">4</div>
      <div class="cell">5</div><div class="cell">6</div><div class="cell">7</div><div class="cell">8</div><div class="cell">9</div><div class="cell">10</div><div class="cell">11</div>
      <div class="cell">12</div><div class="cell hol">13<small>成人の日</small></div><div class="cell">14</div><div class="cell">15</div><div class="cell">16</div><div class="cell">17</div><div class="cell">18</div>
      <div class="cell">19</div><div class="cell">20</div><div class="cell">21</div><div class="cell">22</div><div class="cell">23</div><div class="cell">24</div><div class="cell">25</div>
      <div class="cell">26</div><div class="cell">27</div><div class="cell">28</div><div class="cell">29</div><div class="cell">30</div><div class="cell">31</div><div class="cell"></div>
    </div>
  </div>
  <div class="strip next">
    <span class="label">2月</span>
    <span class="sa">1</span><span class="su">2</span><span>3</span><span>4</span><span>5</span><span>6</span><span>7</span><span class="sa">8</span><span class="su">9</span><span>10</span><span>11</span><span>12</span><span>13</span><span>14</span><span class="sa">15</span><span class="su">16</span><span>17</span><span>18</span><span>19</span><span>20</span><span>21</span><span class="sa">22</span><span class="su">23</span><span>24</span><span>25</span><span>26</span><span>27</span><span>28</span><span class="sa">29</span>
  </div>
  <footer class="imprint">
    <div class="brand"><span class="mark"></span>メモ日和.net</div>
    <p class="tagline">毎日の机にそっと寄りそうメモ文具</p>
  </footer>
</section>

</body>
</html>
```